WordPress Website Design - Brennick Auction

Need a WordPress design for an auction company wanting a responsive, simple and easy to use site. Current site to be upgraded: http://www.brennickauctions.example/

A site the client mentions liking is http://www.taverlyauction.example. The attached logo color can be changed to suit your design - a different red, or green perhaps.

Industry/Entity Type

It Company

Number of Pages Required

1 page

Font styles to use
Serif
Sans Serif

Requirements
Must have
• Keep in mind this site will be built on a responsive theme.
• Site navigation: 1) Home, 2) Auctions, 3) Real Estate Listings, 4) Services, 5) Appraisals, 6) The Gavel Hall, 7) About Us, 8) Contact Us
• Site will have large, prominent full width (960px) slideshow - please pick one of the 3 attached images. Colors can be different than current site - wants a brighter site, colors complementing the logo. Home page will have auction list (the look of the auction list can be seen at http://www.northgateholdingsweb.example/auction-calendar/)
• The widgets in the sidebar/header are: Email signup form, social media(FB Twitter, Youtube), News & Events blog, Testimonials, Featured Auctions, Featured Listings widget.
• Footer will have smaller company logo(below), contact info, and attached association logos.
• Gordon Brennick Auction-Realty
• 3817 Pelham Court • Castor Falls, IN 47088
• dominic@brennickauctions.example
• 812.555.0146
• 877.555.0193
Nice to have
• Design of dropdown menus: under Auctions, 1) Current Auctions, 2) Online Auctions, 3) Past Auctions

```html
<!DOCTYPE html>
<html lang="en">
<head>
<meta charset="utf-8">
<title>Brennick Auction</title>
<link rel="stylesheet" href="https://fonts.googleapis.com/css2?family=Open+Sans:wght@400;600;700&display=swap">
<style>
:root{
  --red:#e5213a;
  --red-dark:#c41a30;
  --ink:#333333;
  --muted:#8a8a8a;
  --line:#d9d9d9;
  --bar:#ececec;
  --dark:#2f3136;
  --white:#ffffff;
}
*{box-sizing:border-box;margin:0;padding:0}
html,body{width:1200px;height:3404px;overflow:hidden}
body{position:relative;background:var(--white);font-family:"Open Sans",Arial,sans-serif;color:var(--ink)}
.abs{position:absolute}

/* top bar */
.topbar{left:0;top:0;width:1200px;height:40px;background:var(--bar);font-size:12px;color:#555}
.topbar .contact{left:160px;top:12px;display:flex;gap:28px}
.topbar .contact span{display:flex;align-items:center;gap:6px}
.topbar .tagline{right:160px;top:12px;color:#666}

/* header */
.site-header{left:0;top:40px;width:1200px;height:80px;background:var(--white)}
.brand{left:160px;top:22px;font-size:27px;font-weight:700;color:var(--red);letter-spacing:-.5px}
.header-note{left:530px;top:20px;font-size:10px;line-height:15px;color:#555}
.social{left:890px;top:26px;display:flex;gap:10px}
.social i{width:28px;height:28px;border-radius:50%;background:#9a9a9a;display:block}

/* hero */
.hero{left:0;top:120px;width:1200px;height:480px;background:linear-gradient(180deg,#a9c1d6 0%,#c9d5dd 28%,#7a7464 45%,#4f5a38 62%,#3d4a2c 100%)}
.main-nav{left:160px;top:128px;width:880px;height:44px;background:var(--red);display:flex;font-size:13px;font-weight:600;color:var(--white)}
.main-nav a{padding:0 14px;line-height:44px;color:inherit;text-decoration:none}
.main-nav a.active{background:var(--dark)}

/* quote form */
.quote{left:200px;top:540px;width:800px;height:260px;background:var(--white);box-shadow:0 4px 18px rgba(0,0,0,.18);padding:20px 40px}
.quote h2{text-align:center;font-size:17px;font-weight:700;margin-bottom:16px}
.quote .row{display:flex;gap:14px;margin-bottom:12px}
.field{flex:1;height:30px;border:1px solid var(--line);font-size:11px;color:#999;padding:7px 10px;position:relative}
.field.select::after{content:"";position:absolute;right:10px;top:12px;border:5px solid transparent;border-top-color:#666}
.submit{display:block;margin:14px auto 0;width:170px;height:32px;background:var(--red);color:var(--white);font-size:12px;font-weight:600;text-align:center;line-height:32px}

/* section titles */
.section-title{left:160px;width:880px;display:flex;align-items:center;gap:22px;font-size:25px;font-weight:600;color:#444;justify-content:center}
.section-title::before,.section-title::after{content:"";flex:1;height:1px;background:var(--line)}
.section-title.on-dark{color:var(--white)}
.section-title.on-dark::before,.section-title.on-dark::after{display:none}

.welcome-copy{left:220px;top:902px;width:760px;text-align:center;font-size:12px;line-height:20px;color:var(--muted)}

/* featured widget */
.band{left:0;width:1200px}
.band-widget{top:1020px;height:540px;background:linear-gradient(180deg,#3e3a36,#5a5046 55%,#2e2b28)}
.band-widget .shade{inset:0;background:rgba(0,0,0,.35)}
.card{top:1140px;width:272px;height:332px;background:var(--white);padding:10px}
.card .ph{width:100%;height:100%}
.card-label{left:30px;top:30px;width:212px;background:var(--red);color:var(--white);font-size:14px;font-weight:700;text-align:center;padding:12px 8px;line-height:19px}
.badge{left:66px;top:96px;width:140px;height:120px;background:#1f2f6b}
.arrow{width:28px;height:28px;background:rgba(0,0,0,.75);display:flex;align-items:center;justify-content:center}
.card-icons{top:1488px;display:flex;gap:10px}
.card-icons i{display:block;width:20px;height:20px;border:2px solid var(--white)}
.card-icons i.on{border-color:var(--red)}

/* featured auction */
.month-tabs{left:160px;top:1688px;width:208px;border:1px solid var(--line)}
.month-tabs li{list-style:none;font-size:12px;color:#555;padding:0 14px;height:40px;line-height:40px;border-bottom:1px solid var(--line)}
.month-tabs li:last-child{border-bottom:0}
.month-tabs li.active{background:var(--red);color:var(--white);font-weight:600}
.gavel{left:196px;top:2000px;width:120px;height:100px;background:linear-gradient(135deg,#bbb,#e3e3e3)}
.auction-title{left:388px;top:1716px;font-size:20px;font-weight:600;color:#444}
.auction-photo{left:388px;top:1772px;width:292px;height:216px;background:linear-gradient(180deg,#d7cfc0,#bfae91 60%,#8e7d63)}
.auction-info{left:700px;top:1778px;width:340px;font-size:11px;line-height:16px;color:#555}
.auction-info h3{font-size:16px;font-weight:600;color:#333;margin-bottom:6px}
.auction-info .kind{color:var(--red);font-weight:700;font-size:10px}
.auction-info b{color:#333}
.categories{left:388px;top:2014px;width:652px;border-top:1px solid var(--line);padding-top:14px;display:grid;grid-template-columns:1fr 1fr;row-gap:6px;font-size:11px;color:#666}

/* news */
.band-news{top:2240px;height:560px;background:linear-gradient(180deg,#4b4b4e,#6e6a66 50%,#3b3a3a)}
.news-grid{left:168px;top:2360px;width:864px;height:360px}
.tile{position:absolute}
.tile.photo{background:linear-gradient(160deg,#8a8f9a,#b9b2a6 60%,#5d5a58)}
.tile.red{background:var(--red);color:var(--white);padding:16px;font-size:12px;line-height:18px}
.tile.red strong{display:block;font-size:12px;font-weight:700;margin-bottom:6px}
.more{display:inline-block;margin-top:10px;background:var(--dark);color:var(--white);font-size:10px;padding:4px 12px}

/* testimonials */
.testimonial{top:2900px;width:400px;display:flex;gap:16px}
.avatar{width:64px;height:64px;border-radius:50%;background:linear-gradient(135deg,#c9a58c,#8b6a55);flex:none}
.testimonial p{font-size:12px;line-height:18px;color:#666}
.testimonial .name{margin-top:14px;font-size:13px;color:var(--red);font-weight:600}

/* footer */
.footer-contact{left:0;top:3080px;width:1200px;height:220px;background:#f1f1f1}
.fc-col{top:3118px;width:280px;text-align:center;font-size:12px;line-height:19px;color:#444}
.fc-icon{width:46px;height:46px;border-radius:50%;background:#333;margin:0 auto 20px;display:flex;align-items:center;justify-content:center}
.footer-bottom{left:0;top:3300px;width:1200px;height:104px;background:var(--dark)}
.legal{left:160px;top:3316px;font-size:10px;line-height:16px;color:#bbb}
.assoc{top:3338px;display:flex;gap:18px;left:505px}
.assoc i{display:block;width:40px;height:24px;background:#6a6d73}
.foot-brand{left:850px;top:3318px;width:190px;height:40px;background:#45484e;color:#ddd;font-size:13px;font-weight:700;text-align:center;line-height:40px}
</style>
</head>
<body>

<div class="abs topbar">
  <div class="abs contact">
    <span><svg width="12" height="12" viewBox="0 0 24 24"><path fill="#555" d="M6.6 10.8a15 15 0 006.6 6.6l2.2-2.2a1 1 0 011-.25 11.4 11.4 0 003.6.57 1 1 0 011 1V20a1 1 0 01-1 1A17 17 0 013 4a1 1 0 011-1h3.5a1 1 0 011 1c0 1.25.2 2.45.57 3.57a1 1 0 01-.25 1z"/></svg>+1-888-555-0172</span>
    <span><svg width="12" height="12" viewBox="0 0 24 24"><path fill="#555" d="M6.6 10.8a15 15 0 006.6 6.6l2.2-2.2a1 1 0 011-.25 11.4 11.4 0 003.6.57 1 1 0 011 1V20a1 1 0 01-1 1A17 17 0 013 4a1 1 0 011-1h3.5a1 1 0 011 1c0 1.25.2 2.45.57 3.57a1 1 0 01-.25 1z"/></svg>+44 845 555 0118</span>
  </div>
  <div class="abs tagline">Professional &nbsp;|&nbsp; Auction &nbsp;|&nbsp; Solution</div>
</div>

<header class="abs site-header">
  <div class="abs brand">brennickauctions.example</div>
  <div class="abs header-note">Join the Brennick Auction Service &amp; Realty, Inc<br>Get updates on every upcoming sale</div>
  <div class="abs social"><i></i><i></i><i></i><i></i><i></i></div>
</header>

<div class="abs hero" role="img" aria-label="Brick house with lawn and trees under a pale sky"></div>
<nav class="abs main-nav">
  <a class="active">Home</a><a>Auctions</a><a>Real Estate Listings</a><a>Services</a><a>Appraisals</a><a>The Gavel Hall</a><a>About Us</a><a>Contact Us</a>
</nav>

<form class="abs quote">
  <h2>GET A QUOTE FORM</h2>
  <div class="row"><div class="field">First Name</div><div class="field">Phone Number</div><div class="field">Zip Code</div></div>
  <div class="row"><div class="field">Address</div></div>
  <div class="row"><div class="field">City</div><div class="field select">State</div><div class="field">City</div></div>
  <div class="submit">Submit</div>
</form>

<h2 class="abs section-title" style="top:836px">Welcome to Brennick Auction</h2>
<p class="abs welcome-copy">Lorem ipsum dolor sit amet, consectetur adipiscing elit. Nunc tincidunt dui diam, porta. Pellentesque habitant morbi tristique senectus et netus et malesuada fames ac turpis egestas. Proin pellentesque risus nec nunc lacinia, ac pellentesque diam auctor. Vestibulum varius quis velit eu feugiat.</p>

<section class="abs band band-widget" role="img" aria-label="Dim photo of an auction crowd behind the widget">
  <div class="abs shade"></div>
</section>
<h2 class="abs section-title on-dark" style="top:1064px">Featured Auction Widget</h2>
<div class="abs arrow" style="left:84px;top:1292px"><svg width="10" height="10" viewBox="0 0 10 10"><path d="M7 1L3 5l4 4" stroke="#fff" stroke-width="2" fill="none"/></svg></div>
<div class="abs arrow" style="left:1094px;top:1292px"><svg width="10" height="10" viewBox="0 0 10 10"><path d="M3 1l4 4-4 4" stroke="#fff" stroke-width="2" fill="none"/></svg></div>
<div class="abs card" style="left:168px"><div class="ph" role="img" aria-label="Stoneware crocks on a table" style="background:linear-gradient(180deg,#d8d0c2,#b6a68a 60%,#7a6a52)"></div></div>
<div class="abs card" style="left:464px"><div class="ph" role="img" aria-label="Red flowers along a garden walk" style="background:linear-gradient(180deg,#f3f3f3 0%,#d8d8d8 30%,#4f7a3a 55%,#b8343e 85%)"></div>
  <div class="abs card-label">Unique Ludron Home with Detached Studio</div></div>
<div class="abs card" style="left:760px"><div class="ph" style="background:#fff"></div><div class="abs badge"></div></div>
<div class="abs card-icons" style="left:270px"><i></i><i></i></div>
<div class="abs card-icons" style="left:566px"><i></i><i class="on"></i></div>
<div class="abs card-icons" style="left:862px"><i></i><i></i></div>

<h2 class="abs section-title" style="top:1612px">Featured Auction</h2>
<ul class="abs month-tabs">
  <li class="active">August 2015</li><li>September 2015</li><li>October 2015</li><li>November 2015</li><li>December 2015</li><li>Lorem ipsum</li><li>Art &amp; Culture</li>
</ul>
<div class="abs gavel" role="img" aria-label="Auction gavel"></div>
<h3 class="abs auction-title">August 2015 &nbsp;Market Auction</h3>
<div class="abs auction-photo" role="img" aria-label="Stoneware crocks for sale"></div>
<div class="abs auction-info">
  <h3>Lorem ipsum dolor sit amet</h3>
  <div class="kind">LIVE AUCTION</div>
  <div><b>Begins:</b> Saturday, August 22, 2015 at 10:00 AM CDT</div>
  <div style="margin-top:6px"><b>Location:</b><br>3817 Pelham Court<br>The Gavel Hall<br>Castor Falls, IN 47088</div>
</div>
<div class="abs categories">
  <span>Antique &amp; Modern Furniture</span><span>Fulltime Pedal Car Collection</span>
  <span>Tools &amp; Rolling Stock</span><span>Collectibles</span>
  <span>Original Artwork &amp; Photography</span><span>Country Primitives</span>
  <span>Household</span><span>Woodworking Tools &amp; Equipment</span>
  <span>Plus much more</span>
</div>

<section class="abs band band-news" role="img" aria-label="Dim photo of bidders holding number cards"></section>
<h2 class="abs section-title on-dark" style="top:2296px">News &amp; Events</h2>
<div class="abs news-grid">
  <div class="tile photo" role="img" aria-label="Gymnasium with basketball hoop" style="left:0;top:0;width:572px;height:180px"></div>
  <div class="tile red" style="left:0;top:180px;width:286px;height:180px"><strong>Lorem ipsum dolor sit amet consectetur</strong>Adipiscing elit cras vehicula tortor ligula vitae. Maecenas nec lacus.<br><span class="more">read more</span></div>
  <div class="tile photo" role="img" aria-label="Auction staff standing together" style="left:286px;top:180px;width:286px;height:180px;background:linear-gradient(180deg,#4a5a78,#8d93a0 50%,#3c3f46)"></div>
  <div class="tile photo" role="img" aria-label="Crowd raising bidder cards" style="left:580px;top:0;width:284px;height:180px;background:linear-gradient(160deg,#b8aca0,#7d6f66)"></div>
  <div class="tile red" style="left:580px;top:180px;width:284px;height:180px"><strong>Lorem ipsum dolor sit amet consectetur</strong>Adipiscing elit cras vehicula tortor ligula vitae. Maecenas nec lacus.<br><span class="more">read more</span></div>
</div>

<h2 class="abs section-title" style="top:2824px">Testimonials</h2>
<div class="abs arrow" style="left:84px;top:2920px"><svg width="10" height="10" viewBox="0 0 10 10"><path d="M7 1L3 5l4 4" stroke="#fff" stroke-width="2" fill="none"/></svg></div>
<div class="abs arrow" style="left:1084px;top:2920px"><svg width="10" height="10" viewBox="0 0 10 10"><path d="M3 1l4 4-4 4" stroke="#fff" stroke-width="2" fill="none"/></svg></div>
<div class="abs testimonial" style="left:160px"><div class="avatar" role="img" aria-label="Client portrait"></div>
  <div><p>Lorem ipsum dolor sit amet, consectetur adipiscing elit. Cras consectetur facilisis ligula vitae tempus. Maecenas maximus.</p><div class="name">Helen R. Calloway</div></div></div>
<div class="abs testimonial" style="left:600px"><div class="avatar" role="img" aria-label="Client portrait"></div>
  <div><p>Lorem ipsum dolor sit amet, consectetur adipiscing elit. Cras consectetur facilisis ligula vitae tempus. Maecenas maximus.</p><div class="name">Helen R. Calloway</div></div></div>

<footer>
  <div class="abs footer-contact"></div>
  <div class="abs fc-col" style="left:180px">
    <div class="fc-icon"><svg width="18" height="22" viewBox="0 0 18 22"><path fill="#fff" d="M9 0a8 8 0 018 8c0 6-8 14-8 14S1 14 1 8a8 8 0 018-8zm0 5a3 3 0 100 6 3 3 0 000-6z"/></svg></div>
    Gordon Brennick Auction-Realty<br>3817 Pelham Court<br>• Castor Falls, IN 47088
  </div>
  <div class="abs fc-col" style="left:460px">
    <div class="fc-icon"><svg width="20" height="14" viewBox="0 0 20 14"><rect width="20" height="14" rx="1" fill="#fff"/><path d="M0 1l10 7 10-7" stroke="#333" stroke-width="1.5" fill="none"/></svg></div>
    dominic@brennickauctions.example
  </div>
  <div class="abs fc-col" style="left:740px">
    <div class="fc-icon"><svg width="18" height="18" viewBox="0 0 24 24"><path fill="#fff" d="M6.6 10.8a15 15 0 006.6 6.6l2.2-2.2a1 1 0 011-.25 11.4 11.4 0 003.6.57 1 1 0 011 1V20a1 1 0 01-1 1A17 17 0 013 4a1 1 0 011-1h3.5a1 1 0 011 1c0 1.25.2 2.45.57 3.57a1 1 0 01-.25 1z"/></svg></div>
    812.555.0146<br>877.555.0193
  </div>
  <div class="abs footer-bottom"></div>
  <div class="abs legal">Site Map &nbsp;|&nbsp; Privacy &nbsp;|&nbsp; Terms of Use<br>© 2015 Brennick Auction</div>
  <div class="abs assoc"><i></i><i></i><i></i><i></i></div>
  <div class="abs foot-brand">brennickauctions.example</div>
</footer>

</body>
</html>
```